Architecture firm needing a business card

We need a business card design for a new company based in the US called "Pellmore Architecture". Seeking minimalist designs that have a creativity/design feel but must be clean and professional. Please refer to the logo attached.

Target Market(s)

Real Estate Investors, Home Builders and Construction Firms.

Industry/Entity Type

Architecture

Contact Information for Business Card

Standard US size business cards. Would like to have some sort of graphic on the back side of the card - nothing that is too loud but something that may catch your attention. More or less grayscale colors that are in line with the logo colors (navy and greys essentially). Additional colors maybe accepted if blended properly (earthtones), but might be difficult to accomplish and maintain the clean/minimalist look.

Requirements
Must have
• Clean Lines
Nice to have
• some sort of graphics, would like to have something creative on the back side of the card
Should not have
• nothing too busy, cluttered or overwhelming.

```html
<!DOCTYPE html>
<html lang="en">
<head>
<meta charset="utf-8">
<title>Pellmore Architecture – Business Card</title>
<link href="https://fonts.googleapis.com/css2?family=Open+Sans:wght@400;600;700&display=swap" rel="stylesheet">
<style>
  :root {
    --page: #ece9e4;
    --silver-light: #e4e4e4;
    --silver-dark: #b9b9b9;
    --navy: #1d4a72;
    --navy-deep: #0c2240;
    --navy-light: #2f6f99;
    --ink-white: #ffffff;
    --grey-text: #5c6a78;
    --divider: #a7a7a7;
    --building-light: #9fb6c8;
    --building-dark: #5c7d98;
  }
  * { box-sizing: border-box; margin: 0; padding: 0; }
  html, body { width: 1200px; height: 913px; overflow: hidden; }
  body {
    background: var(--page);
    font-family: "Open Sans", Arial, sans-serif;
    position: relative;
  }
  .card {
    position: absolute;
    width: 560px;
    height: 320px;
    border-radius: 22px;
    overflow: hidden;
    box-shadow: 0 8px 24px rgba(0,0,0,0.18);
  }
  .card-front {
    left: 50px; top: 110px;
    background: linear-gradient(160deg, var(--silver-light), var(--silver-dark));
  }
  .card-back {
    left: 590px; top: 480px;
    background: linear-gradient(170deg, var(--navy-light) 0%, var(--navy) 45%, var(--navy-deep) 100%);
  }
  .brand {
    position: absolute;
    display: flex;
    align-items: center;
    gap: 12px;
    font-weight: 600;
    line-height: 1;
  }
  .brand-square { flex: none; border: 3px solid currentColor; }
  .brand-name { letter-spacing: 0.06em; text-transform: uppercase; }
  .brand-name span { display: block; }
  .card-front .brand { left: 36px; top: 132px; color: var(--navy); }
  .card-front .brand-square { width: 30px; height: 30px; }
  .card-front .brand-name span:first-child { font-size: 38px; }
  .card-front .brand-name span:last-child { font-size: 15px; letter-spacing: 0.3em; margin-top: 6px; }
  .divider {
    position: absolute; left: 300px; top: 48px;
    width: 1px; height: 224px; background: var(--divider);
  }
  .contact { position: absolute; left: 318px; top: 52px; color: var(--ink-white); }
  .contact-name { font-size: 19px; font-weight: 700; letter-spacing: 0.03em; }
  .contact-role { font-size: 12px; font-weight: 700; color: var(--navy); letter-spacing: 0.05em; margin-bottom: 14px; }
  .contact-address { font-size: 12.5px; line-height: 1.45; margin-bottom: 14px; }
  .contact-list { list-style: none; font-size: 12.5px; line-height: 1.7; }
  .contact-list li { display: flex; align-items: center; gap: 8px; }
  .contact-list svg { width: 11px; height: 11px; fill: var(--grey-text); flex: none; }
  .card-back .brand { left: 56px; top: 150px; color: var(--ink-white); }
  .card-back .brand-square { width: 40px; height: 40px; }
  .card-back .brand-name span:first-child { font-size: 50px; }
  .card-back .brand-name span:last-child { font-size: 18px; letter-spacing: 0.32em; margin-top: 8px; }
  .building-visual {
    position: absolute; right: 0; top: 0;
    width: 200px; height: 170px;
    background: linear-gradient(200deg, var(--building-light), var(--building-dark) 60%, transparent);
    clip-path: polygon(30% 0, 100% 0, 100% 100%, 10% 100%);
    opacity: 0.75;
  }
</style>
</head>
<body>
  <section class="card card-front">
    <div class="brand">
      <div class="brand-square"></div>
      <div class="brand-name"><span>Pellmore</span><span>Architecture</span></div>
    </div>
    <div class="divider"></div>
    <div class="contact">
      <p class="contact-name">DARA WHITLOW</p>
      <p class="contact-role">OWNER</p>
      <p class="contact-address">1180 Elm Ridge Rd<br>OH 44120, United States</p>
      <ul class="contact-list">
        <li><svg viewBox="0 0 24 24"><path d="M6.6 10.8a15 15 0 0 0 6.6 6.6l2.2-2.2a1 1 0 0 1 1-.25 11.4 11.4 0 0 0 3.6.6 1 1 0 0 1 1 1V20a1 1 0 0 1-1 1A17 17 0 0 1 3 4a1 1 0 0 1 1-1h3.5a1 1 0 0 1 1 1c0 1.25.2 2.45.6 3.6a1 1 0 0 1-.25 1z"/></svg>+1 555 0142-737</li>
        <li><svg viewBox="0 0 24 24"><path d="M2 5h20v14H2zm2 2v.5l8 5 8-5V7zm0 2.8V17h16V9.8l-8 5z"/></svg>info@darawhitlow.com</li>
        <li><svg viewBox="0 0 24 24"><circle cx="12" cy="12" r="10"/></svg>www.pellmorearch.com</li>
      </ul>
    </div>
  </section>

  <section class="card card-back">
    <div class="building-visual" role="img" aria-label="Upward view of a modern glass high-rise building"></div>
    <div class="brand">
      <div class="brand-square"></div>
      <div class="brand-name"><span>Pellmore</span><span>Architecture</span></div>
    </div>
  </section>
</body>
</html>
```